Dog Food Bag Packaging Redesign

Hey there..We're a small dog food company, focusing on all natural, locally sourced, high quality ingredients. They're patties, and baked for 10 min. Dogs go insane for them. We're looking to redo our packaging, and thus, its design. I've attached images. Currently, we are wrapping 12 patties in a poly bag and then butcher paper, and sticking a label on it. We're moving to a zipper seal poly that's black. I've attached the design concept from our bag manufacturer for your reference only. We don't necessarily want to use our old label, but we're not against using elements of it. We really like our current label.. I'm just not so sure it's the right call for a poly bag.We have three flavours; chicken, beef, lamb. I would LOVE to know what flavour the bag is without having to be super close to the bag. So perhaps the top part (1-4 inches) could be the flavour colour? I will have to provide some verbiage for the back. I need to add feeding instructions, and a bit of a thank you story. I'm open for suggestions on how to display ingredients/nutritional facts.

Target Market(s)

Dog Owners

Industry/Entity Type

Manufacturing

Font styles to use
Sans Serif

Colors
9bcb3c

Requirements
Must have
• Total bag design. When you submit your design, please submit your designs on top of a bag. It makes it much easier to visual the end product.
• The bag needs to have the associated flavour colours on it to differentiate flavour from a distance. Red = beef, yellow = chicken, purple = lamb.
• I'm happy with the logo being on the back only, but if on the front it needs to be small. Patties should be the main header word.
Nice to have
• I like the idea of a vertical colour bar on the side of the bag to show its flavour, but I'm not again a top horizontal bar either.
• I like PATTIES being the biggest word on the bag.

```html
<!DOCTYPE html>
<html lang="en">
<head>
<meta charset="utf-8">
<title>Patties — Flavour Range</title>
<link rel="stylesheet" href="https://fonts.googleapis.com/css2?family=Montserrat:wght@700;800&family=PT+Sans+Narrow:wght@400;700&display=swap">
<style>
  :root{
    --backdrop:#8c8c8c;
    --pouch:#f1f1f1;
    --pouch-edge:#dcdcdc;
    --ink:#1b1919;
    --paper:#f7f7f7;
    --text-dark:#222;
    --chicken:#e8a423;
    --beef:#d91c4a;
    --lamb:#a4399c;
    --fur:#b0763e;
    --fur-dark:#5a3a22;
  }
  *{box-sizing:border-box;margin:0;padding:0}
  html,body{width:1200px;height:618px;overflow:hidden}
  body{
    background:var(--backdrop);
    display:flex;justify-content:center;align-items:center;gap:56px;
    font-family:"PT Sans Narrow",sans-serif;
  }
  .pouch{
    width:320px;height:520px;
    background:linear-gradient(180deg,var(--pouch),#e6e6e6);
    border:1px solid var(--pouch-edge);
    border-radius:6px 6px 18px 18px;
    position:relative;
    display:flex;justify-content:center;
  }
  .pouch--chicken{--flavour:var(--chicken)}
  .pouch--beef{--flavour:var(--beef)}
  .pouch--lamb{--flavour:var(--lamb)}
  .zip-seal{
    position:absolute;left:18px;right:18px;top:30px;height:40px;
    border-top:3px solid #e0e0e0;border-bottom:3px solid #e0e0e0;
  }
  .label{
    position:absolute;top:95px;width:248px;height:390px;
    background:var(--paper);
    overflow:hidden;
  }
  .label__head{
    height:122px;background:var(--ink);
    display:flex;flex-direction:column;align-items:center;
  }
  .count-badge{
    width:44px;height:32px;background:var(--flavour);color:#fff;
    border-radius:0 0 9px 9px;
    font:400 22px/32px "PT Sans Narrow",sans-serif;text-align:center;
  }
  .tagline{
    margin-top:10px;color:#eee;font-size:12px;letter-spacing:2px;
  }
  .brand-title{
    margin-top:4px;color:#fff;
    font:800 37px/1 "Montserrat",sans-serif;letter-spacing:3px;
  }
  .flavour-pill{
    position:absolute;top:103px;left:50%;transform:translateX(-50%);
    width:136px;height:56px;border-radius:9px;
    background:var(--flavour);color:#fff;text-align:center;
  }
  .flavour-pill__cut{
    display:block;margin-top:5px;font-size:12px;letter-spacing:4.5px;opacity:.9;
  }
  .flavour-pill__name{
    display:block;margin-top:1px;font:700 25px/1 "Montserrat",sans-serif;letter-spacing:.5px;
  }
  .ingredients{
    margin:50px 10px 0;text-align:center;color:var(--text-dark);
    font-size:11px;line-height:17px;font-weight:700;letter-spacing:1px;
  }
  .maker{
    margin-top:10px;display:flex;flex-direction:column;align-items:center;gap:2px;
  }
  .maker__dot{width:13px;height:13px;border-radius:50%;background:#9bcb3c}
  .maker__name{font-size:9px;font-weight:700;color:var(--text-dark);letter-spacing:1px}
  .rating{margin-top:6px;text-align:center;font-size:11px;letter-spacing:6px;color:var(--ink)}
  .dog-photo{
    position:absolute;left:20px;right:20px;bottom:24px;height:88px;
    background:radial-gradient(ellipse at 50% 70%,var(--fur) 0%,#8a5a30 55%,var(--fur-dark) 100%);
    border-radius:50% 50% 0 0/60% 60% 0 0;
  }
  .flavour-band{position:absolute;left:8px;right:8px;bottom:4px;height:36px}
</style>
</head>
<body>

  <section class="pouch pouch--chicken">
    <div class="zip-seal"></div>
    <div class="label">
      <header class="label__head">
        <div class="count-badge">12</div>
        <p class="tagline">fresh • local • responsible</p>
        <h1 class="brand-title">PATTIES</h1>
      </header>
      <div class="flavour-pill"><span class="flavour-pill__cut">deboned</span><span class="flavour-pill__name">CHIKEN</span></div>
      <p class="ingredients">deboned chiken, fresh eggs, apples, fresh<br>potatoes, broccoli, carrots</p>
      <div class="maker"><span class="maker__dot"></span><span class="maker__name">HOLLOWFIELD</span></div>
      <p class="rating">★★★★★</p>
      <div class="dog-photo" role="img" aria-label="Photo of a brown dog's eyes and nose peeking up over the colour band"></div>
      <svg class="flavour-band" viewBox="0 0 232 36" preserveAspectRatio="none"><path d="M0 6 H232 V22 Q116 40 0 22 Z" fill="var(--flavour)"/></svg>
    </div>
  </section>

  <section class="pouch pouch--beef">
    <div class="zip-seal"></div>
    <div class="label">
      <header class="label__head">
        <div class="count-badge">12</div>
        <p class="tagline">fresh • local • responsible</p>
        <h1 class="brand-title">PATTIES</h1>
      </header>
      <div class="flavour-pill"><span class="flavour-pill__cut">gras-fed</span><span class="flavour-pill__name">BEEF</span></div>
      <p class="ingredients">grass-fed beef, fresh eggs, apples, fresh<br>potatoes, broccoli, carrots</p>
      <div class="maker"><span class="maker__dot"></span><span class="maker__name">HOLLOWFIELD</span></div>
      <p class="rating">★★★★★</p>
      <div class="dog-photo" role="img" aria-label="Photo of a brown dog's eyes and nose peeking up over the colour band"></div>
      <svg class="flavour-band" viewBox="0 0 232 36" preserveAspectRatio="none"><path d="M0 6 Q116 -4 232 6 V22 Q116 40 0 22 Z" fill="var(--flavour)"/></svg>
    </div>
  </section>

  <section class="pouch pouch--lamb">
    <div class="zip-seal"></div>
    <div class="label">
      <header class="label__head">
        <div class="count-badge">12</div>
        <p class="tagline">fresh • local • responsible</p>
        <h1 class="brand-title">PATTIES</h1>
      </header>
      <div class="flavour-pill"><span class="flavour-pill__cut">deboned</span><span class="flavour-pill__name">LAMB</span></div>
      <p class="ingredients">deboned lamb, fresh eggs, apples, fresh<br>potatoes, broccoli, carrots</p>
      <div class="maker"><span class="maker__dot"></span><span class="maker__name">HOLLOWFIELD</span></div>
      <p class="rating">★★★★★</p>
      <div class="dog-photo" role="img" aria-label="Photo of a brown dog's eyes and nose peeking up over the colour band"></div>
      <svg class="flavour-band" viewBox="0 0 232 36" preserveAspectRatio="none"><path d="M0 6 Q116 -4 232 6 V22 Q116 40 0 22 Z" fill="var(--flavour)"/></svg>
    </div>
  </section>

</body>
</html>
```